"Sun On Water" Gospel Presentation Booklet

I need a design for a 12 page (including front/back cover) square booklet, with religious images and aesthetically pleasing fonts/designs. I want it to be very simple, and very straightforward. The main focus of the project is it's content. So the design should be very nice, but also should point to the content, not take away from it, or create distraction. People should be more focused on the words than the imagery.

I enjoy modern designs, I need a sharp aesthetic that is clean and neat. Nothing over the top.
I have attached a word document with the content I would like on the pages.

Colors
0592cd
0255a3
33a6d7
85cae6
85acd3
3276b5
9bcb3b
f04a50
f68d4c

Requirements
Should not have
• Super feminine colors/aesthetics

```html
<!DOCTYPE html>
<html lang="en">
<head>
<meta charset="UTF-8">
<title>Man — Problem</title>
<link href="https://fonts.googleapis.com/css2?family=Anton&family=Work+Sans:wght@300;400;700&display=swap" rel="stylesheet">
<style>
  :root {
    --paper: #ffffff;
    --ink: #000000;
    --orange: #f68d4c;
    --green: #9bcb3b;
    --light: #ffffff;
    --rule: #dddddd;
    --photo-tone-1: #9a9a9a;
    --photo-tone-2: #7a7a7a;
    --scene-tone-1: #d45a74;
    --scene-tone-2: #c24a64;
  }
  * { margin: 0; padding: 0; box-sizing: border-box; }
  html, body { width: 1200px; height: 1200px; overflow: hidden; background: var(--paper); }
  .spread {
    position: relative;
    width: 1200px; height: 1200px;
    display: grid;
    grid-template-columns: 600px 600px;
    grid-template-rows: 600px 600px;
  }
  .page { position: relative; overflow: hidden; }
  .title-page { background: var(--paper); }
  .title-page svg { position: absolute; inset: 0; }
  .title-word { font-family: "Anton", "Oswald", sans-serif; fill: var(--ink); }
  .title-page--top { border-bottom: 1px solid var(--rule); }

  .content-page { color: var(--light); font-family: "Work Sans", "Helvetica Neue", Arial, sans-serif; }
  .content-page--man { background: var(--orange); }
  .content-page--problem { background: var(--green); }

  .headline {
    position: absolute; left: 0; right: 0;
    text-align: center; font-weight: 700;
    text-transform: uppercase; letter-spacing: -0.2px;
  }
  .content-page--man .headline { top: 48px; font-size: 28.5px; line-height: 31px; }
  .content-page--problem .headline { top: 85px; font-size: 28px; line-height: 32px; }

  .photo-area {
    position: absolute;
    background: linear-gradient(180deg, var(--photo-tone-1), var(--photo-tone-2));
  }
  .photo-area--walker { left: 133px; top: 137px; width: 122px; height: 390px; }

  .example-text {
    position: absolute; left: 267px; top: 230px;
    font-size: 27px; line-height: 33.5px; font-weight: 400;
  }
  .example-text strong, .body-text strong { font-weight: 700; }

  .body-text {
    position: absolute; left: 0; right: 0; top: 155px;
    text-align: center; font-size: 21.5px; line-height: 29.2px; font-weight: 300;
  }
  .scene-area {
    position: absolute; left: 0; right: 0; top: 385px; bottom: 0;
    background: linear-gradient(180deg, var(--scene-tone-1), var(--scene-tone-2));
  }
</style>
</head>
<body>
<main class="spread">
  <section class="page title-page title-page--top">
    <svg width="600" height="600" viewBox="0 0 600 600">
      <text class="title-word" x="81" y="418" font-size="249" textLength="438" lengthAdjust="spacingAndGlyphs">MAN</text>
    </svg>
  </section>

  <section class="page content-page content-page--man">
    <h2 class="headline">On the other hand,<br>mankind is corrupt.</h2>
    <div class="photo-area photo-area--walker" role="img" aria-label="Photo of a young man in a white T-shirt walking away, casting a long shadow"></div>
    <p class="example-text">For example,<br>we are <strong>SELFISH</strong>,<br>we are <strong>PRIDEFUL</strong>,<br>and we <strong>LIE</strong>.</p>
  </section>

  <section class="page title-page">
    <svg width="600" height="600" viewBox="0 0 600 600">
      <text class="title-word" x="42" y="366" font-size="138" textLength="516" lengthAdjust="spacingAndGlyphs">PROBLEM</text>
    </svg>
  </section>

  <section class="page content-page content-page--problem">
    <h2 class="headline">And there is our big problem:</h2>
    <p class="body-text">if God is perfect and corruption cannot<br>live with him...and we are corrupt...<br><strong>WE</strong> cannot live with God.<br>Our corruption has cut us<br>off from God...now...<strong>AND</strong> when we die<br>which means we must spend eternity<br>in a place called hell...</p>
    <div class="scene-area" role="img" aria-label="Photo of a person sitting hunched over in the corner of a pink curved wall"></div>
  </section>
</main>
</body>
</html>
```